BOLD & MINIMALIST DESIGN NEEDED

We want a very bold but minimalistic business card design that is impactful and utilizes both sides of the business card. Our current logo is included for your use.

We want bold fonts and good use of negative space. We don't want the logo to overpower the design.

Target Market(s)

Professionals who are building new commercial buildings.

Industry/Entity Type

Construction

Contact Information for Business Card

Name, Title, email, office phone, cell phone, website

Font styles to use
Serif
Sans Serif

Requirements
Must have
• Bold design!

```html
<!DOCTYPE html>
<html lang="en">
<head>
<meta charset="utf-8">
<title>Stonemark Business Card</title>
<link rel="stylesheet" href="https://fonts.googleapis.com/css2?family=Poppins:ital,wght@0,400;0,500;0,700;0,800;1,300&display=swap">
<style>
  :root {
    --backdrop: #dcdcdc;
    --ink: #0a0b0d;
    --paper: #ffffff;
    --lime: #8cc63f;
    --rule: #5a5a5a;
  }
  * { margin: 0; padding: 0; box-sizing: border-box; }
  html, body { width: 1200px; height: 1200px; overflow: hidden; background: var(--backdrop); }
  body { position: relative; font-family: "Poppins", sans-serif; }

  .card {
    position: absolute;
    width: 901px;
    height: 515px;
    border-radius: 31px;
    overflow: hidden;
    background: var(--paper);
  }
  .card--front { left: 149px; top: 57px; }
  .card--back { left: 151px; top: 627px; }

  .brand {
    position: absolute;
    left: 0; right: 0;
    display: flex;
    align-items: center;
    justify-content: center;
    gap: 18px;
  }
  .brand__mark { width: 30px; height: 30px; background: var(--lime); }
  .brand__name { font-weight: 800; color: var(--ink); letter-spacing: 2px; line-height: 1; }
  .card--front .brand { top: 160px; }
  .card--front .brand__name { font-size: 78px; }

  .tagline-band {
    position: absolute;
    left: 0; right: 0;
    top: 400px;
    height: 56px;
    background: var(--ink);
    display: flex;
    align-items: center;
    justify-content: center;
  }
  .tagline {
    color: var(--lime);
    font-style: italic;
    font-weight: 300;
    font-size: 34px;
    line-height: 1;
  }

  .contact-panel {
    position: absolute;
    left: 0; top: 0;
    width: 497px; height: 100%;
    background: var(--ink);
  }
  .person { position: absolute; left: 72px; top: 58px; }
  .person__name { color: var(--paper); font-weight: 700; font-size: 50px; line-height: 1; }
  .person__title {
    color: var(--lime);
    font-weight: 700;
    font-size: 34px;
    letter-spacing: 6px;
    line-height: 1;
    margin-top: 14px;
    padding-bottom: 10px;
    border-bottom: 1px solid var(--rule);
    width: 232px;
    white-space: nowrap;
  }
  .contact-list { position: absolute; left: 72px; top: 220px; list-style: none; }
  .contact-list li {
    display: flex;
    align-items: center;
    height: 38px;
    margin-bottom: 28px;
    color: var(--paper);
    font-size: 27px;
    font-weight: 400;
  }
  .contact-list .icon {
    width: 38px; height: 38px;
    border-radius: 50%;
    background: var(--paper);
    display: flex; align-items: center; justify-content: center;
    margin-right: 21px;
    flex: none;
  }
  .contact-list svg { width: 22px; height: 22px; }

  .card--back .brand { left: 497px; top: 238px; gap: 12px; }
  .card--back .brand__name { font-size: 44px; }
  .card--back .brand__mark { width: 18px; height: 18px; }
</style>
</head>
<body>
  <section class="card card--front">
    <div class="brand">
      <span class="brand__mark"></span>
      <span class="brand__name">STONEMARK</span>
    </div>
    <div class="tagline-band">
      <p class="tagline">Innovative Design. Solid Construction.</p>
    </div>
  </section>

  <section class="card card--back">
    <div class="contact-panel">
      <div class="person">
        <h1 class="person__name">Your Name</h1>
        <p class="person__title">Your Title</p>
      </div>
      <ul class="contact-list">
        <li>
          <span class="icon">
            <svg viewBox="0 0 24 24" fill="none" stroke="#0a0b0d" stroke-width="1.8"><rect x="3" y="4" width="4" height="16" rx="1"/><rect x="9" y="6" width="12" height="14" rx="1"/><path d="M12 10h6M12 13h1M15 13h1M18 13h0M12 16h1M15 16h1"/></svg>
          </span>+1 (000) 000-0000
        </li>
        <li>
          <span class="icon">
            <svg viewBox="0 0 24 24" fill="none" stroke="#0a0b0d" stroke-width="1.6" stroke-linejoin="round"><path d="M5 3l4 1 1 5-2 1.5a11 11 0 0 0 5.5 5.5L15 14l5 1 1 4-2 2C10 21 3 14 3 5z"/></svg>
          </span>+1 (000) 000-0000
        </li>
        <li>
          <span class="icon">
            <svg viewBox="0 0 24 24" fill="none" stroke="#0a0b0d" stroke-width="1.6"><rect x="3" y="6" width="18" height="12"/><path d="M3 6l9 7 9-7M3 18l7-6M21 18l-7-6"/></svg>
          </span>your email here
        </li>
        <li>
          <span class="icon">
            <svg viewBox="0 0 24 24" fill="none" stroke="#0a0b0d" stroke-width="1.5"><circle cx="12" cy="12" r="9"/><ellipse cx="12" cy="12" rx="4" ry="9"/><path d="M3 12h18M4.5 7.5h15M4.5 16.5h15"/></svg>
          </span>your website here
        </li>
      </ul>
    </div>
    <div class="brand">
      <span class="brand__mark"></span>
      <span class="brand__name">STONEMARK</span>
    </div>
  </section>
</body>
</html>
```